nutrition ebook cover

i need a cover for a ebook designed, the book is called Amber Lattice so i would like that somewhere on the cover. i would also like the word nutrition followed by my company logo that i have attached below somewhere on the cover( i have attached two logos and would like to see with both separatley), i would like this to be faded into the background if possible, perhaps in a upper or lower corner. i would also like to see options with and without the picture i have attached below. the look I'm going for is professional and clean. this is a fat loss, healthy eating booklet. the winning designer i would like to design the following pages within the book aswell no more than 10 pages, that i will provide all content for, i just need help with putting what i have on pdf in a way that looks professional and cool. this would ideally covered in the rate that is paid for the cover. i also have other booklets i need made so the winning designer will most likely get that work too at a later date for an additional fee of course.

Industry/Entity Type

Nutrition

Requirements
Nice to have
• Outside images are welcomed, happy to purchase any stock images used from a outside source

```html
<!DOCTYPE html>
<html lang="en">
<head>
<meta charset="utf-8">
<title>Amber Lattice – Fat Loss Nutrition Booklet</title>
<link rel="stylesheet" href="https://fonts.googleapis.com/css2?family=Josefin+Sans:wght@300;400&family=Alegreya:wght@400&display=swap">
<style>
  :root {
    --cover-orange: #e4532c;
    --ribbon-white: #ffffff;
    --text-white: #ffffff;
    --slate-dark: #5d6a6e;
    --slate-light: #a9b3b2;
    --wood-warm: #b48a6a;
    --wood-light: #d9bfa6;
  }
  * { margin: 0; padding: 0; box-sizing: border-box; }
  html, body { width: 927px; height: 1200px; overflow: hidden; }
  body { background: #ffffff; }

  .cover {
    position: relative;
    width: 927px;
    height: 1200px;
    overflow: hidden;
  }

  .cover-photo {
    position: absolute;
    inset: 0;
    background:
      radial-gradient(ellipse 420px 560px at 720px 760px, var(--wood-light) 0%, var(--wood-warm) 55%, rgba(180,138,106,0) 100%),
      radial-gradient(ellipse 300px 260px at 420px 160px, rgba(240,236,226,0.85) 0%, rgba(240,236,226,0) 100%),
      radial-gradient(ellipse 200px 300px at 90px 900px, rgba(150,175,120,0.7) 0%, rgba(150,175,120,0) 100%),
      linear-gradient(160deg, var(--slate-light) 0%, var(--slate-dark) 60%, #7b7f78 100%);
    filter: saturate(0.9);
  }

  .title-disc {
    position: absolute;
    left: 167px;
    top: 303px;
    width: 592px;
    height: 592px;
    border-radius: 50%;
    background: var(--cover-orange);
    opacity: 0.94;
  }

  .disc-content {
    position: absolute;
    left: 167px;
    top: 303px;
    width: 592px;
    height: 592px;
    color: var(--text-white);
    text-align: center;
  }

  .brand-name {
    position: absolute;
    top: 80px;
    left: 0;
    width: 100%;
    font-family: "Josefin Sans", sans-serif;
    font-weight: 400;
    font-size: 17px;
    letter-spacing: 2px;
    text-transform: uppercase;
  }

  .book-title {
    position: absolute;
    top: 128px;
    left: 0;
    width: 100%;
    font-family: "Josefin Sans", sans-serif;
    font-weight: 300;
    font-size: 44px;
    letter-spacing: 1px;
  }

  .rule {
    position: absolute;
    left: 136px;
    width: 320px;
    height: 12px;
  }
  .rule--top { top: 222px; }
  .rule--bottom { top: 358px; }

  .headline {
    position: absolute;
    top: 236px;
    left: 0;
    width: 100%;
    font-family: "Alegreya", serif;
    font-weight: 400;
    font-size: 92px;
    line-height: 112px;
  }

  .ribbon {
    position: absolute;
    top: 420px;
    left: 83px;
    width: 428px;
    height: 62px;
  }

  .ribbon-label {
    position: absolute;
    top: 420px;
    left: 83px;
    width: 428px;
    height: 62px;
    line-height: 64px;
    font-family: "Josefin Sans", sans-serif;
    font-weight: 400;
    font-size: 29px;
    color: var(--cover-orange);
  }

  .subject {
    position: absolute;
    top: 506px;
    left: 0;
    width: 100%;
    font-family: "Josefin Sans", sans-serif;
    font-weight: 400;
    font-size: 30px;
  }
</style>
</head>
<body>
  <main class="cover">
    <div class="cover-photo" role="img" aria-label="Blurred overhead photo of fresh vegetables — potatoes, leeks, mushrooms, tomatoes, chillies and herbs — around a wooden chopping board on a slate surface"></div>

    <div class="title-disc"></div>

    <div class="disc-content">
      <div class="brand-name">Kelpworks</div>
      <h1 class="book-title">Amber Lattice</h1>

      <svg class="rule rule--top" viewBox="0 0 320 12" aria-hidden="true">
        <path d="M0 3 Q80 1 160 3 T320 3" fill="none" stroke="#fff" stroke-width="2"/>
        <path d="M10 9 Q90 7 170 9 T310 9" fill="none" stroke="#fff" stroke-width="1.2"/>
      </svg>

      <h2 class="headline">fat loss</h2>

      <svg class="rule rule--bottom" viewBox="0 0 320 12" aria-hidden="true">
        <path d="M10 3 Q90 1 170 3 T310 3" fill="none" stroke="#fff" stroke-width="1.2"/>
        <path d="M0 9 Q80 7 160 9 T320 9" fill="none" stroke="#fff" stroke-width="2"/>
      </svg>

      <svg class="ribbon" viewBox="0 0 428 62" aria-hidden="true">
        <polygon points="0,0 428,0 400,31 428,62 0,62 28,31" fill="#ffffff"/>
      </svg>
      <div class="ribbon-label">• healthy booklet •</div>

      <p class="subject">nutrition</p>
    </div>
  </main>
</body>
</html>
```